Vessa Almond Protein - Less, but better

Design a protein powder pouch (350g). Take inspiration from Brimora.co and put the same information on the pouch and add "made in Australia". I do not want it to be exactly the same design but just take some inspiration from it.

```html
<!DOCTYPE html>
<html lang="en">
<head>
<meta charset="utf-8">
<title>Vessa Almond Protein Powder – Pouch Front</title>
<link href="https://fonts.googleapis.com/css2?family=Montserrat:wght@600;700;800&family=Poppins:wght@300;400;500;600&display=swap" rel="stylesheet">
<style>
  :root {
    --backdrop: #ffffff;
    --sage: #7fa399;
    --sage-light: #9bb8ae;
    --blush: #d6a29f;
    --blush-light: #e2b5b2;
    --cream: #f3efe4;
    --gold: #c48d35;
    --gold-dark: #b07a27;
    --forest: #2f4c43;
    --forest-deep: #1f3830;
    --label-ink: #f6ece8;
  }
  html, body {
    margin: 0;
    width: 1200px;
    height: 900px;
    overflow: hidden;
    background: var(--backdrop);
  }
  .canvas {
    position: relative;
    width: 1200px;
    height: 900px;
    font-family: "Poppins", sans-serif;
  }
  .pouch {
    position: absolute;
    left: 372px;
    top: 88px;
    width: 456px;
    height: 690px;
    border-radius: 16px 16px 6px 6px;
    overflow: hidden;
    background: linear-gradient(100deg, var(--sage-light) 0%, var(--sage) 45%, var(--sage) 100%);
  }
  .pouch__lower {
    position: absolute;
    left: 0;
    top: 0;
    width: 456px;
    height: 690px;
  }
  .pouch__zip {
    position: absolute;
    left: 0;
    top: 82px;
    width: 100%;
    height: 2px;
    background: rgba(40, 70, 60, 0.12);
  }
  .brand {
    position: absolute;
    top: 82px;
    width: 100%;
    text-align: center;
    font-family: "Poppins", sans-serif;
    font-weight: 500;
    font-size: 86px;
    line-height: 1;
    letter-spacing: 1px;
    color: var(--cream);
  }
  .tagline {
    position: absolute;
    top: 186px;
    width: 100%;
    text-align: center;
    font-weight: 300;
    font-size: 22px;
    letter-spacing: 1px;
    color: var(--cream);
  }
  .seal {
    position: absolute;
    left: 84px;
    top: 233px;
    width: 278px;
    height: 278px;
    border-radius: 50%;
    background: var(--cream);
  }
  .seal__title {
    position: absolute;
    width: 100%;
    text-align: center;
    font-family: "Montserrat", sans-serif;
    font-weight: 700;
    line-height: 1;
    margin: 0;
  }
  .seal__title--almond { top: 68px; font-size: 40px; color: var(--gold); }
  .seal__title--protein { top: 113px; font-size: 40px; color: var(--forest); }
  .seal__title--powder { top: 155px; font-size: 40px; color: var(--forest-deep); }
  .flavour {
    position: absolute;
    left: 60px;
    top: 199px;
    width: 160px;
    height: 18px;
    background: linear-gradient(90deg, var(--gold) 0%, var(--gold-dark) 100%);
    color: #fff;
    font-size: 14px;
    font-weight: 500;
    line-height: 18px;
    text-align: center;
    letter-spacing: 0.3px;
  }
  .claims {
    position: absolute;
    top: 224px;
    width: 100%;
    text-align: center;
    font-size: 7.5px;
    font-weight: 500;
    color: var(--forest-deep);
  }
  .badge {
    position: absolute;
    left: 349px;
    top: 479px;
    width: 48px;
    height: 72px;
    border-radius: 7px;
    background: var(--forest-deep);
  }
  .badge__amount {
    position: absolute;
    left: 3px;
    top: 3px;
    width: 42px;
    height: 38px;
    border-radius: 5px 5px 0 0;
    background: var(--cream);
    color: var(--forest-deep);
    font-family: "Montserrat", sans-serif;
    font-weight: 700;
    font-size: 22px;
    line-height: 38px;
    text-align: center;
  }
  .badge__label {
    position: absolute;
    top: 45px;
    width: 100%;
    text-align: center;
    color: #fff;
    font-size: 8px;
    font-weight: 500;
    line-height: 9px;
  }
  .divider {
    position: absolute;
    left: 204px;
    top: 538px;
    width: 48px;
    height: 2px;
    background: var(--label-ink);
  }
  .benefits {
    position: absolute;
    top: 550px;
    width: 100%;
    text-align: center;
    font-size: 12.5px;
    line-height: 16px;
    color: var(--label-ink);
  }
  .origin {
    position: absolute;
    top: 607px;
    width: 100%;
    text-align: center;
    font-size: 12px;
    letter-spacing: 3px;
    color: var(--label-ink);
  }
  .net-weight {
    position: absolute;
    top: 636px;
    width: 100%;
    text-align: center;
    font-size: 11.5px;
    color: var(--label-ink);
  }
</style>
</head>
<body>
<main class="canvas">
  <section class="pouch" aria-label="Vessa Almond Protein pouch front">
    <svg class="pouch__lower" viewBox="0 0 456 690" aria-hidden="true">
      <defs>
        <linearGradient id="blushFill" x1="0" y1="0" x2="1" y2="0">
          <stop offset="0" stop-color="#e2b5b2"/>
          <stop offset="0.5" stop-color="#d6a29f"/>
          <stop offset="1" stop-color="#cf9995"/>
        </linearGradient>
      </defs>
      <path d="M0 478 Q228 462 456 468 L456 690 L0 690 Z" fill="url(#blushFill)"/>
    </svg>
    <div class="pouch__zip"></div>

    <div class="brand">Vessa</div>
    <div class="tagline">–less, but better–</div>

    <div class="seal">
      <h1 class="seal__title seal__title--almond">ALMOND</h1>
      <p class="seal__title seal__title--protein">PROTEIN</p>
      <p class="seal__title seal__title--powder">POWDER</p>
      <div class="flavour">REAL VANILLA</div>
      <div class="claims">VEGAN | JUST 4 INGREDIENTS | DELICIOUS</div>
    </div>

    <div class="badge">
      <div class="badge__amount">18g</div>
      <div class="badge__label">PLANT<br>PROTEIN</div>
    </div>

    <div class="divider"></div>
    <div class="benefits">
      SUPPORTS HEALTH:<br>
      HEART, DIGESTION, INMUNE SYSTEM,<br>
      SKIN, BONE; HAIR
    </div>
    <div class="origin">MADE IN AUSTRALIA</div>
    <div class="net-weight">NET WT. 350G</div>
  </section>
</main>
</body>
</html>
```